I need a flyer that is professional, advertises and informs people about my health coaching practice. I am a Nationally Board Certified Health and Wellness Coach, lifestyle medicine certified and a lifestyle coach for the NBO's Glucose Readiness Program. I have my Master's Degree in Counseling Psychology. The final design should communicate evidence based health coaching that is self-directed and aimed at creating lasting health behavioral changes designed to enhance well-being. I am very open in terms of design but really would like a professional look to the flyer. I did want my contact information on the flyer: mabel@vitalgroveworks.com and (217) 586-3914

Target Market(s)

Adults looking to improve their health, decrease risk factors for lifestyle disease, reduce weight, make better lifestyle choices to improve well-being.

Industry/Entity Type

Health And Wellness

Font styles to use
Sans Serif

Colors

Designer to choose colors to be used in the design.

Requirements
Must have
• Services offered, a professional feel, Mabel Harlow Health Coaching (name of my practice), my phone number (217) 586-3914 and email: mabel@vitalgroveworks.com, location: 1873 W Larkspur Street Bloomington IL 61709 my website: mabelharlow.com to schedule appointments
Nice to have
• What is Health Coaching? Health and Wellness Coaches partner with clients seeking self-directed, lasting changes, aligned with their values, which promote health and wellness and, thereby, enhance well-being. In the course of their work health and wellness coaches display unconditional positive regard for their clients and a belief in their capacity for change, and honoring that each client is an expert on his or her life, while ensuring that all interactions are respectful and non-judgmental.

```html
<!DOCTYPE html>
<html lang="en">
<head>
<meta charset="utf-8">
<title>Mabel Harlow Health Coaching</title>
<link rel="stylesheet" href="https://fonts.googleapis.com/css2?family=Delius&family=Fira+Sans:wght@300&family=Fredoka:wght@600&family=Satisfy&family=Ubuntu&display=swap">
<style>
  :root {
    --magenta: #d7117f;
    --band: #d9108a;
    --sky-light: #f6f7f8;
    --sky-warm: #f5e6cf;
    --sky-blue: #dfe6ec;
    --meadow: #8f9a7f;
    --figure-light: rgba(250, 246, 242, 0.95);
    --figure-skin: rgba(232, 196, 168, 0.55);
    --ink: #4a4a4a;
    --ink-soft: #6e6e6e;
    --accent-blue: #1ba4da;
    --white: #ffffff;
  }
  * { margin: 0; padding: 0; box-sizing: border-box; }
  html, body { width: 1200px; height: 846px; overflow: hidden; background: var(--white); }
  .flyer { position: relative; width: 1200px; height: 846px; overflow: hidden; }
  .hero-photo {
    position: absolute; inset: 0;
    background:
      radial-gradient(ellipse 130px 330px at 500px 560px, var(--figure-light) 0%, rgba(250,246,242,0) 100%),
      radial-gradient(ellipse 300px 150px at 250px 480px, var(--figure-skin) 0%, rgba(232,196,168,0) 100%),
      radial-gradient(ellipse 110px 130px at 380px 260px, rgba(214,160,110,0.55) 0%, rgba(214,160,110,0) 100%),
      radial-gradient(ellipse 420px 380px at 330px 120px, var(--sky-warm) 0%, rgba(245,230,207,0) 100%),
      linear-gradient(180deg, var(--sky-light) 0%, var(--sky-blue) 70%, #cfd6d3 82%, var(--meadow) 100%);
  }
  .practice-name {
    position: absolute; left: 646px; top: 56px;
    font-family: "Fredoka", sans-serif; font-weight: 600; font-size: 31px;
    color: var(--ink-soft); letter-spacing: 0.3px; white-space: nowrap;
  }
  .headline {
    position: absolute; left: 638px; top: 170px;
    font-family: "Delius", sans-serif; font-weight: 400; font-size: 64px;
    line-height: 73px; color: var(--ink); white-space: nowrap;
  }
  .services {
    position: absolute; left: 646px; top: 410px; display: flex; align-items: center;
    font-family: "Fira Sans", sans-serif; font-weight: 300; font-size: 17px;
    color: var(--accent-blue); white-space: nowrap;
  }
  .services .divider { width: 2px; height: 27px; background: var(--ink); margin: 0 19px; }
  .tagline { position: absolute; left: 0; top: 0; }
  .tagline-text { font-family: "Satisfy", cursive; font-size: 36px; fill: var(--magenta); }
  .contact-band {
    position: absolute; left: 0; top: 694px; width: 1200px; height: 88px;
    background: var(--band); color: var(--white);
    font-family: "Ubuntu", sans-serif; font-size: 17.5px;
  }
  .contact-item { position: absolute; display: flex; align-items: center; white-space: nowrap; }
  .contact-item svg { width: 16px; height: 16px; margin-right: 10px; flex: none; }
  .icon-solid { fill: var(--white); }
  .phone { left: 54px; top: 28px; }
  .email { left: 54px; top: 53px; }
  .address { left: 770px; top: 28px; }
  .website { left: 770px; top: 53px; }
</style>
</head>
<body>
<main class="flyer">
  <div class="hero-photo" role="img" aria-label="Photo of a woman in a white tank top leaning back with arms open under a bright hazy sky above a meadow"></div>

  <h1 class="practice-name">Mabel Harlow Health Coaching</h1>

  <h2 class="headline">Health Coaching<br>is Embracing<br>your Health</h2>

  <div class="services">
    <span>Health Coaching</span><span class="divider"></span>
    <span>Wellness Experience</span><span class="divider"></span>
    <span>Active Coaching</span>
  </div>

  <svg class="tagline" width="1200" height="846" viewBox="0 0 1200 846" aria-label="Let us help you build the healthy life you deserve!">
    <defs>
      <path id="tagline-path" d="M276 568 C 380 508, 560 512, 680 568 S 880 606, 956 546"/>
    </defs>
    <text class="tagline-text" font-family="Satisfy, cursive" textLength="690" lengthAdjust="spacing"><textPath href="#tagline-path">Let us help you build the healthy life you deserve!</textPath></text>
  </svg>

  <footer class="contact-band">
    <div class="contact-item phone">
      <svg class="icon-solid" viewBox="0 0 24 24"><path d="M6.6 10.8a15.1 15.1 0 0 0 6.6 6.6l2.2-2.2a1 1 0 0 1 1-.25 11.4 11.4 0 0 0 3.6.57 1 1 0 0 1 1 1V20a1 1 0 0 1-1 1A17 17 0 0 1 3 4a1 1 0 0 1 1-1h3.5a1 1 0 0 1 1 1c0 1.25.2 2.45.57 3.57a1 1 0 0 1-.25 1z"/></svg>
      <span>(217) 586-3914</span>
    </div>
    <div class="contact-item email">
      <svg viewBox="0 0 24 24"><path d="M2 5h20v14H2z" fill="var(--white)"/><path d="M3.5 6.5 12 13l8.5-6.5" fill="none" stroke="var(--band)" stroke-width="1.5"/></svg>
      <span>email: mabel@vitalgroveworks.com</span>
    </div>
    <div class="contact-item address">
      <svg class="icon-solid" viewBox="0 0 24 24"><path d="M12 2a7 7 0 0 0-7 7c0 5.2 7 13 7 13s7-7.8 7-13a7 7 0 0 0-7-7zm0 9.5A2.5 2.5 0 1 1 12 6.5a2.5 2.5 0 0 1 0 5z"/></svg>
      <span>1873 W Larkspur Street Bloomington IL 61709</span>
    </div>
    <div class="contact-item website">
      <svg viewBox="0 0 24 24" fill="none" stroke="#ffffff" stroke-width="1.6"><circle cx="12" cy="12" r="9.5"/><ellipse cx="12" cy="12" rx="4" ry="9.5"/><path d="M2.5 12h19M4 7h16M4 17h16"/></svg>
      <span>mabelharlow.com</span>
    </div>
  </footer>
</main>
</body>
</html>
```